Business card for Eyelash extension salon in Beverly Hills,California USA

We need new business card for our salon in Beverly Hills. The salon name is 'Lumarra' . We would like to have...Business name: Lumarra Name of person: will provide later Address 6128 N.Corbel Ridge Blvd Beverly Hills , CA 90210 Phone: will provide later (Text only) Web: www.lumarrastudio-example.com Pictogrid icon, Friendvale icon follow us for seasonal campaign and news @lumarrastudioexample Design should look elegant, high-end, clean, simple, cohesive with my brand. Please refer my brand board. Business name color will be metallic bronzy color. Im thinking grey background or white background. Thanks

Target Market(s)

25-35. Gender neutral. People who are in Entertainment business industry.
This is High-end Eyelash extension salon in Beverly Hills

Industry/Entity Type

Beauty Salon

Contact Information for Business Card

Business name: Lumarra
Name of person: will provide later
Address 6128 N.Corbel Ridge Blvd Beverly Hills , CA 90210
Phone: will provide later (Text only)
Web: www.lumarrastudio-example.com
Pictogrid icon, Friendvale icon
follow us for seasonal campaign and news @lumarrastudioexample

Requirements
Must have
• Beautiful, elegant, clean and simple look but very attractive and modern
Should not have
• We don't like too clutter, too busy designs.

```html
<!DOCTYPE html>
<html lang="en">
<head>
<meta charset="utf-8">
<title>Lumarra – Business Card</title>
<link href="https://fonts.googleapis.com/css2?family=Jost:wght@500;600;700&family=PT+Sans:wght@400;700&display=swap" rel="stylesheet">
<style>
  :root {
    --card-bg: #ecebe8;
    --ink: #3b3a39;
    --bronze: #a2734b;
    --social-dot: #a2734b;
    --art-tone: #d9d6d1;
    --art-soft: rgba(217, 214, 209, 0);
  }
  * { margin: 0; padding: 0; box-sizing: border-box; }
  html, body {
    width: 1018px;
    height: 1200px;
    overflow: hidden;
    background: var(--card-bg);
  }
  .card {
    position: relative;
    width: 1018px;
    height: 1200px;
    background: var(--card-bg);
    color: var(--ink);
    font-family: "PT Sans", sans-serif;
    overflow: hidden;
  }
  .tools-art-top {
    position: absolute;
    left: 0;
    top: 0;
    width: 500px;
    height: 600px;
    border-bottom-right-radius: 220px;
    background: radial-gradient(ellipse at 30% 40%, var(--art-tone) 0%, var(--art-soft) 85%);
  }
  .tools-art-bottom {
    position: absolute;
    left: 0;
    bottom: 0;
    width: 1018px;
    height: 140px;
    background: linear-gradient(to top, var(--art-tone), var(--art-soft));
  }
  .follow {
    position: absolute;
    right: 72px;
    top: 38px;
    font-family: "Jost", sans-serif;
    font-weight: 600;
    font-size: 26px;
  }
  .social {
    position: absolute;
    left: 662px;
    top: 92px;
    list-style: none;
  }
  .social li {
    display: flex;
    align-items: center;
    height: 40px;
    margin-bottom: 15px;
    font-size: 22px;
  }
  .social .dot {
    width: 40px;
    height: 40px;
    border-radius: 50%;
    background: var(--social-dot);
    margin-right: 9px;
    flex: none;
  }
  .social .network {
    position: absolute;
    width: 1px; height: 1px;
    overflow: hidden;
    clip: rect(0 0 0 0);
  }
  .brand {
    position: absolute;
    right: 60px;
    top: 410px;
    text-align: right;
  }
  .brand-name {
    font-family: "Jost", sans-serif;
    font-weight: 700;
    font-size: 64px;
    line-height: 1.1;
    color: var(--bronze);
  }
  .tagline {
    margin-top: 38px;
    font-size: 23px;
    letter-spacing: 0.3px;
  }
  .person {
    position: absolute;
    left: 0;
    top: 720px;
    width: 1018px;
    text-align: center;
  }
  .person-name {
    font-family: "Jost", sans-serif;
    font-weight: 600;
    font-size: 54px;
    letter-spacing: 1px;
    line-height: 1.1;
  }
  .role {
    margin-top: 34px;
    font-weight: 700;
    font-size: 28px;
    letter-spacing: 4px;
  }
  .contact {
    margin-top: 30px;
    font-size: 24px;
    line-height: 34.5px;
  }
  .contact .web { font-size: 28px; line-height: 40px; }
</style>
</head>
<body>
  <div class="card">
    <div class="tools-art-top" role="img" aria-label="Line illustration of beauty tools: comb, scissors and dryer"></div>
    <div class="tools-art-bottom" role="img" aria-label="Line illustration of beauty tools along the bottom edge"></div>

    <p class="follow">follow us for seasonal campaign and news</p>
    <ul class="social">
      <li><span class="dot"></span><span class="network">Friendvale</span>@lumarrastudioexample</li>
      <li><span class="dot"></span><span class="network">Pictogrid</span>@lumarrastudioexample</li>
    </ul>

    <div class="brand">
      <h1 class="brand-name">Lumarra</h1>
      <p class="tagline">FOR ALL YOUR LASH CARE NEEDS</p>
    </div>

    <div class="person">
      <h2 class="person-name">Rowan Ashby</h2>
      <p class="role">LASH ARTIST</p>
      <div class="contact">
        <p>Mobile: 123-456-7890</p>
        <p>Address: 6128 N.Corbel Ridge Blvd Beverly Hills ,<br>CA 90210</p>
        <p>Email: hello@lumarrastudio-example.com</p>
        <p class="web">Website: www.lumarrastudio-example.com</p>
      </div>
    </div>
  </div>
</body>
</html>
```